Business Card for Professional Photographer

I'm looking for an eye catching modern clean design that compliments my logo/ website fonts & colours.
I specialise in architecture, corporate & commercial photography so I'm marketing to professional clients rather than portrait / wedding clients.

I would prefer to not have a solid black design.

My logo brand guide is as follows :

Main front font. : Reislust
Main font colour : #fff
Slogan front font : Ubuntu Bold
Monogram front font : Venti Medium
Container colour : #fff

I need print ready files in pdf .png & .eps formats.

Included in the files below are some screen grabs as reference to font & colours etc.

```html
<!DOCTYPE html>
<html lang="en">
<head>
<meta charset="utf-8">
<title>Lumen Frame – Business Card</title>
<link rel="stylesheet" href="https://fonts.googleapis.com/css2?family=Ubuntu:wght@400;700&family=Roboto:wght@400&display=swap">
<style>
  :root {
    --bg: #3a3a3a;
    --card-black: #232323;
    --card-black-deep: #1c1c1c;
    --gold-dark: #c1924a;
    --gold-mid: #dcb96a;
    --gold-light: #f3e79f;
    --silver: #b9b9b9;
    --ink: #111111;
  }
  * { box-sizing: border-box; margin: 0; padding: 0; }
  html, body { width: 799px; height: 1200px; overflow: hidden; }
  body {
    background: var(--bg);
    font-family: "Roboto", Arial, sans-serif;
    position: relative;
  }
  .card {
    position: absolute;
    left: 80px;
    width: 640px;
    height: 366px;
    border-radius: 4px;
    overflow: hidden;
    box-shadow: 0 14px 30px rgba(0,0,0,.45);
  }
  .card--front { top: 150px; background: var(--card-black); }
  .card--back  { top: 690px; background: var(--card-black); }

  /* front */
  .brand-lockup {
    position: absolute;
    left: 0; right: 0; top: 130px;
    display: flex; align-items: center; justify-content: center; gap: 14px;
  }
  .brand-lockup__dot {
    width: 22px; height: 22px; border-radius: 50%;
    border: 3px solid currentColor;
  }
  .brand-lockup__name {
    font-family: "Ubuntu", Arial, sans-serif;
    font-weight: 700;
    font-size: 40px;
    letter-spacing: 1px;
  }
  .card--front .brand-lockup { color: var(--silver); }
  .front-url {
    position: absolute; left: 0; right: 0; bottom: 64px;
    text-align: center;
    font-family: "Ubuntu", Arial, sans-serif;
    font-size: 17px; letter-spacing: 3px;
    color: var(--gold-mid);
  }

  /* back */
  .back-shape { position: absolute; inset: 0; }
  .profile {
    position: absolute; left: 40px; top: 34px; color: var(--ink);
  }
  .profile__name {
    font-family: "Ubuntu", Arial, sans-serif;
    font-weight: 700; font-size: 25px; letter-spacing: -0.3px;
  }
  .profile__role {
    margin-top: 6px; font-size: 15px; line-height: 18px;
  }
  .contact {
    position: absolute; left: 40px; bottom: 60px;
    list-style: none; color: var(--ink); font-size: 16px;
  }
  .contact li { display: flex; align-items: center; gap: 12px; line-height: 22px; }
  .contact svg { width: 13px; height: 13px; fill: var(--ink); flex: none; }
  .card--back .brand-lockup {
    left: 360px; right: 0; top: 160px; color: var(--gold-mid);
  }
  .card--back .brand-lockup__name { font-size: 32px; }
  .card--back .brand-lockup__dot { width: 18px; height: 18px; }
</style>
</head>
<body>
  <section class="card card--front" aria-label="Card front">
    <div class="brand-lockup">
      <span class="brand-lockup__dot"></span>
      <span class="brand-lockup__name">Lumen Frame</span>
    </div>
    <p class="front-url">www.lumenframe.com.au</p>
  </section>

  <section class="card card--back" aria-label="Card back">
    <svg class="back-shape" width="640" height="366" viewBox="0 0 640 366">
      <defs>
        <linearGradient id="goldPanel" x1="0" y1="0" x2="0.3" y2="1">
          <stop offset="0" stop-color="var(--gold-dark)"/>
          <stop offset="0.5" stop-color="var(--gold-mid)"/>
          <stop offset="1" stop-color="var(--gold-light)"/>
        </linearGradient>
      </defs>
      <path d="M0 0 H350 C300 100 280 230 282 366 H0 Z" fill="url(#goldPanel)"/>
      <path d="M350 0 C300 100 280 230 282 366" fill="none" stroke="var(--gold-light)" stroke-width="5"/>
    </svg>

    <div class="profile">
      <h1 class="profile__name">Daniel Marsh</h1>
      <p class="profile__role">Architecture Corporate<br>Commercial Photographer</p>
    </div>

    <ul class="contact">
      <li><svg viewBox="0 0 16 16"><path d="M2 5c0-2 2-3 6-3s6 1 6 3v1h-3V5H5v1H2z M3 8h10l1 6H2z"/></svg>0412 550 718</li>
      <li><svg viewBox="0 0 16 16"><path d="M1 3h14v10H1z M2 4l6 5 6-5" fill="none" stroke="#111" stroke-width="1.6"/></svg>info@lumenframe.com.au</li>
      <li><svg viewBox="0 0 16 16"><circle cx="8" cy="8" r="6.5" fill="none" stroke="#111" stroke-width="1.5"/><path d="M1.5 8h13M8 1.5c-3 3-3 10 0 13M8 1.5c3 3 3 10 0 13" fill="none" stroke="#111" stroke-width="1.2"/></svg>www.lumenframe.com.au</li>
    </ul>

    <div class="brand-lockup">
      <span class="brand-lockup__dot"></span>
      <span class="brand-lockup__name">Lumen Frame</span>
    </div>
  </section>
</body>
</html>
```